Leading the way in online fitness and education requires power house web design

If you need to contact me you can do so via
skype: Travlin

We need a website designed for new company based in Houston Texas called "TravlinFit". We offer web based training and nutrition programs for our members for example we use the same software as these companies: http://marobelka.com/ http://www.liftquorra.com/ i would like my visitors to be captivated by the level of design creativity of the site.

colors to use would be grey, orange and green.
for example i like the green of this site http://www.cartbeam.com/
i will upload my logo files so you can get a feel for shades of grey and orange.

there is a 3d effect filter i would like applied to my logo for use in the web design i have uploaded what that effect looks like.

i will need your designs to be complete with all interior pages which will include Home, Fitness, Nutrition, Fit Lounge, Fit Score, Fit School, Contact Us, Sign up.

fit lounge on my site is the same as pathwick on liftquorra and locker room on marobelka just re branded.

fit school is a research corner for members to learn about health and fitness, we are members of major medical journals on health and fitness and will have all our articles be from the newest research findings.

competitor sites
these sites use same software:
http://marobelka.com/
http://www.liftquorra.com/

these sites are other software.
http://home.sprintmesa.com/software-for-athletes.aspx
http://www.vigordex.com/

here are some websites that i like:
http://www.crestwaveplay.com/
http://www.nub-lantern.com/
http://fimzol.com/
http://www.parqudo.com/
http://www.lortavi.de/fandiloop/
http://brisketmade.com/

i also like the greens in this site that i am uploading

I have been reviewing the designs and would like to update everyone at once I do not want a normal fitness website design style, no testimonials, blog post, bodyfat calculator

my website will be a membership based website. i want the website to sell the main points of my fitness app that my members will have access to look at the comments for my selling points, use those points in the site create designs and graphics to visualize those points.

look at these sites and gain inspiration

http://www.tuvelo.com.pl/#/projekty/case-studies
http://www.quendar.com/en#/home#ld-kpvm-402617-0045
http://www.nub-lantern.com/
http://fimzol.com/
http://www.parqudo.com/

i have a few designers asking me what the selling points are, the website needs to be built around these points

main selling points.

overview

programs utilize the best multi-joint exercises combined with high intensity cardio, to give you a full-body workout, efficiently and effectively. This means you’re burning more calories and building more lean muscle per unit of time than traditional weight training and cardio programs.

When you sign up, you''ll receive a work out and diet plan to fit your goals and fitness level. As you progress through your plan, you can use the personal fitness and meal calendar to record your results. When you sign-up we''ll ask you a series of questions and your workouts will be tailored to your exact needs. That means never having to use a generic diet and exercise plan again.

If you''ve ever tried to lose weight and build muscle and didn''t succeed, we feel your pain. Until now, trying to navigate all the fitness fads and latest trends on your own has been difficult. The best option - hiring a certified personal trainer - may be out of your financial reach. That''s where we come in - we''re personal trainers on a mission to help you reach your fitness goals quickly and for less money than in person training. Best of all, we''re here to help you day or night.

Fitness

Personal Fitness Calendar

Tailored to the member’s schedule and flexible to accommodate any changes to a member’s regular fitness schedule. Track your progress and stay on track with your fitness goals.

Custom Fitness Plan

Based on a member’s current physical condition and goals.

• Step by step exercise instructions
• 3-D video demonstrations of over 600 exercises, including functional and body-weight only movements
• Equipment filter can customize plans to your gym’s equipment package
• Record workouts to track exercise history and progression

Nutrition

Nutritional Assessment

Daily recommended caloric intake (Protein, Carbohydrates and Fats), based on personal profile and daily fitness plan.

Custom Meal Plan

Personalized meal plan based on nutritional assessment.

• Choose number of meals per day
• Add dietary restrictions, food preferences or dislikes
• Database of thousands of ingredients allows for hundreds of thousands of meal combinations
• Include favorite foods by entering custom nutritional information

Weight tracking

Calculate goal weight and track weight-loss or weight-gain progress. You will reach your goals in no time.

Fit Lounge

What is the most important part of any workout or fitness program? Staying motivated. And what better form of motivation than positive encouragement from your peers?

Fit Lounge is fitness focused social network for health-minded individuals looking for a simple and convenient place to track their workout goals and monitor their progress. A unique system of motivation, support and accountability makes setting fitness goals and then keeping up with them easy

Track

Start by setting fitness goals that you want to track. They can be anything from running and jogging to how many hours of sleep you are getting and how many glasses of water you are drinking every day. Other members of the travlinfits community might be tracking the same workout goals as you, so you can always join their groups as well.

Share

Once you start tracking your workout goals, you can share your progress with your friends. Reach a new max on your bench press? Let everyone know. Eclipse the 10 mile mark on your daily run? Spread the word! The communication of encouragement back and forth is a great way to ensure that everyone stays on track with their workout goals.

Achieve

Of course, the point of any workout or fitness program is to achieve the goals you’ve set. And with help from travlinfits workout tracking tools and encouragement from the community, you will achieve your workout goals in no time. When you see a friend has achieved his or her fitness goals, you can send them a virtual “fist bump” as a sign of congratulations. The number of “fist bumps” each user accumulates will be displayed on their profile, providing additional motivation and a healthy dose of competition.

Reason: i dont feel the designs i have received are of the quality i am looking for

check this website out, i know its flash, but i also know you can get creative without flash and have nice effects throughout the site.

http://www.driftlane-hub.com/

I dont want plain jane designs, insert the content i provided into the site and have it explored in a unique way. take as much time on the design as you need as i will keep extending deadline until i find one that is perfect.

as said before don't make the site anything like the competition sites, its only purpose is to sell the memberships using content provided so i need an innovative way to for them to explore that content,

as your designing this site add me on skype so i can detail and help brainstorm ideas my skype id is travlin
you can stray from the color scheme a little or throw it away if you want i just want to see how creative you can get.

Industry/Entity Type

School

Requirements
Nice to have
• if you notice at the bottom of http://marobelka.com/ she has the orange bar with the three short content parts, i like the idea of having a space like that for similar content.

on http://www.vigordex.com/ if you look to the left side of the scrolling icons i like the idea of having icons or animated pictures to point of key benefits.

```html
<!DOCTYPE html>
<html lang="en">
<head>
<meta charset="utf-8">
<title>TravlinFit – Personal Training</title>
<link rel="stylesheet" href="https://fonts.googleapis.com/css2?family=Arimo:ital,wght@0,400;0,700;1,400&family=Oswald:wght@400;500&family=Yanone+Kaffeesatz:wght@300;400&display=swap">
<style>
:root{
  --orange:#f06a1b;
  --orange-dark:#d8550c;
  --green-nav-top:#4fb041;
  --green-nav-bot:#2e8a27;
  --green-deep:#0f4a0c;
  --green-mid:#3f8a2c;
  --green-light:#7ab24e;
  --ink:#1c1c1c;
  --grey-text:#6b6b6b;
  --panel:#1d1d1d;
  --slate-top:#4e5f73;
  --slate-bot:#3a4656;
  --slate-dark:#2b333d;
  --field:#1f2638;
  --sky:#3aa4dc;
  --steel:#3b5d9a;
  --navy:#1a76b0;
  --white:#ffffff;
}
*{margin:0;padding:0;box-sizing:border-box}
html,body{width:736px;height:1200px;overflow:hidden;background:var(--white)}
body{font-family:"Arimo",Arial,sans-serif;color:var(--ink)}
.page{position:relative;width:736px;height:1200px;overflow:hidden}
.abs{position:absolute}

/* header */
.site-header{position:absolute;left:0;top:0;width:736px;height:106px;background:var(--white)}
.brand{left:84px;top:40px;display:flex;align-items:center;gap:8px}
.brand-dot{width:22px;height:22px;border-radius:50%;background:var(--orange)}
.brand-name{font-weight:700;font-size:26px;color:#3a3a3a;letter-spacing:-.5px}
.account{left:460px;top:10px;font-size:9px;color:#222;display:flex;gap:8px}
.account span+span{border-left:1px solid #ccc;padding-left:8px}
.social-strip{left:544px;top:0;width:118px;height:29px;background:#eeeeee;border-radius:0 0 4px 4px;display:flex;align-items:center;justify-content:space-around;font-size:7px;color:#234}
.mini{display:inline-flex;align-items:center;gap:3px}
.sq{display:inline-flex;align-items:center;justify-content:center;width:10px;height:10px;border-radius:2px;background:var(--steel)}
.sq.sky{background:var(--sky)}
.count{border:1px solid #bbb;background:#fff;padding:0 2px;font-size:6px}
.stay{left:480px;top:51px;font-size:7px;color:#777;display:flex;align-items:center;gap:5px}
.stay .icon{display:inline-flex;align-items:center;justify-content:center;width:15px;height:15px;border-radius:2px;background:var(--sky)}
.stay .icon.blue{background:var(--steel)}
.stay .icon.navy{background:var(--navy)}
.phone{left:546px;top:74px;font-size:18px;color:#111;letter-spacing:-.3px}

/* nav */
.main-nav{position:absolute;left:0;top:106px;width:736px;height:30px;background:linear-gradient(var(--green-nav-top),var(--green-nav-bot));display:flex;align-items:center;padding-left:85px}
.main-nav a{color:#fff;text-decoration:none;font-size:11px;height:30px;line-height:30px;padding:0 18px;position:relative}
.main-nav a+a::before{content:"";position:absolute;left:0;top:9px;height:12px;border-left:1px solid rgba(255,255,255,.45)}
.main-nav a.active{background:var(--orange);padding:0 15px}
.main-nav a.active+a::before{display:none}

/* stage */
.stage{position:absolute;left:0;top:136px;width:736px;height:780px;background:linear-gradient(var(--green-deep) 0%,#1e6216 25%,var(--green-mid) 50%,var(--green-light) 100%)}

.slider{left:74px;top:142px;width:588px;height:344px;background:var(--panel);box-shadow:0 2px 6px rgba(0,0,0,.5)}
.slide-photo{left:80px;top:150px;width:576px;height:287px;
  background:
    radial-gradient(ellipse 26% 60% at 50% 55%,rgba(232,92,130,.55),transparent 70%),
    radial-gradient(ellipse 70% 35% at 50% 48%,rgba(226,184,156,.75),transparent 75%),
    linear-gradient(#b9cad8 0%,#e7eef3 18%,#d9dfe4 30%,#cfb8a8 45%,#8f8f98 62%,#5573a6 74%,#2f5fb4 86%,#2350a0 100%);
  box-shadow:inset 0 0 0 1px rgba(0,0,0,.35)}
.arrow{width:34px;height:34px;border-radius:50%;background:#1e1e1e;top:275px;display:flex;align-items:center;justify-content:center;box-shadow:0 0 0 1px #444}
.caption{left:86px;top:455px;font-size:14.5px;color:var(--orange)}
.thumb{top:444px;height:41px;width:86px}
.thumb.on{outline:2px solid var(--sky)}
.thumb.t1{left:394px;background:linear-gradient(#dfe6ec 0%,#d8b6a4 40%,#c86a8a 60%,#3d65b0 100%)}
.thumb.t2{left:486px;background:linear-gradient(90deg,#e6e6e6 0%,#8d8d8d 35%,#d0d0d0 60%,#6d6d6d 100%)}
.thumb.t3{left:575px;background:radial-gradient(ellipse 40% 70% at 45% 50%,#cfcfcf,transparent 80%),linear-gradient(90deg,#9a9a9a,#e8e8e8)}

.cta-row{left:74px;top:492px;width:588px;height:30px}
.cta-ready{left:14px;top:9px;font-size:10px;color:#fff}
.cta-divider{left:122px;top:0;height:30px;border-left:1px solid rgba(255,255,255,.35)}
.cta-line{left:144px;top:7px;font-size:13.5px;color:#fff}
.btn-start{left:500px;top:2px;width:74px;height:25px;background:linear-gradient(#f9a23c,var(--orange-dark));border-radius:3px;color:#222;font-size:10px;text-align:center;line-height:25px}

/* content */
.content{left:74px;top:526px;width:588px;height:390px;background:var(--white)}
.believe-title{left:86px;top:551px;font-size:12.8px;color:#222;font-weight:400}
.believe-title em{font-style:normal;color:var(--orange)}
.believe-copy{left:86px;top:572px;width:352px;font-size:7.4px;line-height:15.6px;color:#111}
.btn{background:linear-gradient(#6a6a6a,#3c3c3c);color:#fff;border-radius:2px;font-size:7px;text-align:center;box-shadow:0 1px 2px rgba(0,0,0,.4)}
.btn-believe{left:86px;top:656px;width:55px;height:20px;line-height:20px}
.video{left:454px;top:542px;width:196px;height:134px;background:#111;box-shadow:0 1px 4px rgba(0,0,0,.5)}
.video-frame{left:458px;top:545px;width:188px;height:104px;
  background:
    linear-gradient(90deg,transparent 20%,rgba(40,40,40,.55) 24%,transparent 30%,transparent 42%,rgba(40,40,40,.6) 46%,transparent 52%,transparent 62%,rgba(40,40,40,.55) 66%,transparent 72%),
    linear-gradient(#e3e6e0 0%,#cfd6cd 35%,#b7bcb3 65%,#c9cbc4 100%)}
.video-bar{left:454px;top:650px;width:196px;height:26px;background:#1a1a1a}

.card-frame{top:706px;width:173px;height:108px;background:#d9d9d9;border:1px solid #bdbdbd;padding:5px}
.card-photo{width:100%;height:100%;box-shadow:inset 0 0 0 1px rgba(0,0,0,.1)}
.f1{left:88px}.f1 .card-photo{background:radial-gradient(ellipse 45% 60% at 55% 40%,#f0c39b,transparent 75%),linear-gradient(#dbe6f4 0%,#eef2f7 55%,#ffffff 80%,#cfdcea 100%)}
.f2{left:282px}.f2 .card-photo{background:radial-gradient(ellipse 35% 30% at 45% 85%,#9cc45a,transparent 80%),radial-gradient(ellipse 40% 55% at 55% 40%,#e9b996,transparent 80%),linear-gradient(90deg,#6a4630,#a57452 50%,#5b3d2b)}
.f3{left:475px}.f3 .card-photo{background:radial-gradient(ellipse 30% 40% at 30% 40%,#d9486c,transparent 80%),linear-gradient(#f3eeee 0%,#d8d4d6 45%,#4d4f58 80%,#2c2e35 100%)}
.card-title{top:820px;font-family:"Oswald",sans-serif;font-size:13px;color:#4a5560;letter-spacing:.2px;font-weight:400}
.card-copy{top:839px;width:170px;font-size:6.9px;line-height:9px;color:var(--grey-text)}
.card-btn{top:864px;width:52px;height:19px;line-height:19px}

/* footer */
.site-footer{position:absolute;left:0;top:915px;width:736px;height:237px;background:radial-gradient(ellipse at 50% 40%,#5d6e84 0%,var(--slate-top) 40%,var(--slate-bot) 100%)}
.foot-h{font-family:"Yanone Kaffeesatz",sans-serif;font-weight:300;font-size:21px;color:#fff}
.foot-copy{font-size:6.6px;line-height:8px;color:#fff}
.foot-rule{left:94px;top:1093px;width:143px;border-top:1px solid rgba(255,255,255,.25)}
.pill{background:#1d2230;color:#fff;font-style:italic;font-size:7px;border-radius:4px;text-align:center;border:1px solid #59677a}
.tooltip{left:312px;top:967px;width:42px;height:13px;background:#2a2f3a;border-radius:3px;color:#fff;font-size:6.5px;text-align:center;line-height:13px}
.soc{top:985px;width:30px;height:30px;border-radius:4px;background:linear-gradient(#8a94a3,#4f5866);border:1px solid #2c323c;display:flex;align-items:center;justify-content:center;box-shadow:inset 0 1px 0 rgba(255,255,255,.3)}
.field{left:499px;width:136px;background:var(--field);border:1px solid #10141f;border-radius:4px;color:#b8c0d0;font-size:7px;font-style:italic;padding-left:10px;box-shadow:inset 0 1px 3px rgba(0,0,0,.6)}
.news-field{left:297px;top:1099px;width:135px;height:20px;background:var(--field);border-radius:4px;border:1px solid #10141f;color:#b8c0d0;font-size:7px;font-style:italic;line-height:20px;padding-left:10px}
.news-btn{left:396px;top:1099px;width:36px;height:20px;line-height:20px;background:linear-gradient(#6f7988,#3e4653);border-radius:0 4px 4px 0;color:#fff;font-style:italic;font-size:7.5px;text-align:center}

.bottom-bar{position:absolute;left:0;top:1152px;width:736px;height:48px;background:var(--slate-dark);border-top:1px solid #555f6c}
.foot-links{left:73px;top:1174px;display:flex;gap:12px;font-size:8px;font-style:italic;color:#fff}
.copyright{left:472px;top:1174px;font-size:7.6px;color:#fff}
</style>
</head>
<body>
<div class="page">

  <header class="site-header">
    <div class="abs brand"><span class="brand-dot"></span><span class="brand-name">TravlinFit</span></div>
    <div class="abs account"><span>Sign in</span><span>Sign Up</span></div>
    <div class="abs social-strip">
      <span class="mini"><span class="sq"><svg width="6" height="6" viewBox="0 0 10 10"><path d="M5 9 L1 5 A2.2 2.2 0 0 1 5 2 A2.2 2.2 0 0 1 9 5 Z" fill="#fff"/></svg></span>Like <span class="count">19k</span></span>
      <span class="mini"><span class="sq sky"><svg width="6" height="6" viewBox="0 0 10 10"><path d="M5 1 V9 M1 5 H9" stroke="#fff" stroke-width="2"/></svg></span>Follow</span>
    </div>
    <div class="abs stay">Stay updated on our social network
      <span class="icon"><svg width="9" height="9" viewBox="0 0 10 10"><path d="M1 2 H9 V7 H4 L2 9 V7 H1 Z" fill="#fff"/></svg></span>
      <span class="icon blue"><svg width="9" height="9" viewBox="0 0 10 10"><circle cx="5" cy="3.2" r="2.2" fill="#fff"/><path d="M1 9.5 A4 3.5 0 0 1 9 9.5 Z" fill="#fff"/></svg></span>
      <span class="icon navy"><svg width="9" height="9" viewBox="0 0 10 10"><circle cx="2" cy="5" r="1.5" fill="#fff"/><circle cx="8" cy="2" r="1.5" fill="#fff"/><circle cx="8" cy="8" r="1.5" fill="#fff"/><path d="M2 5 L8 2 M2 5 L8 8" stroke="#fff" stroke-width="1"/></svg></span>
    </div>
    <div class="abs phone">0800-5531-904</div>
  </header>

  <nav class="main-nav">
    <a class="active">Home</a><a>Fitness</a><a>Nutrition</a><a>Fit Lounge</a><a>Fit Score</a><a>Fit School</a><a>Contact Us</a>
  </nav>

  <div class="stage"></div>

  <section class="abs slider" aria-label="Featured slides"></section>
  <div class="abs slide-photo" role="img" aria-label="Group of women seated on blue gym mats in a bright fitness studio"></div>
  <div class="abs arrow" style="left:61px"><svg width="12" height="14" viewBox="0 0 12 14"><path d="M8 2 L3 7 L8 12" stroke="#fff" stroke-width="2" fill="none"/></svg></div>
  <div class="abs arrow" style="left:641px"><svg width="12" height="14" viewBox="0 0 12 14"><path d="M4 2 L9 7 L4 12" stroke="#fff" stroke-width="2" fill="none"/></svg></div>
  <div class="abs caption">Motivation, Support for you!</div>
  <div class="abs thumb t1 on" role="img" aria-label="Thumbnail of group fitness class"></div>
  <div class="abs thumb t2" role="img" aria-label="Thumbnail of two athletes in black and white"></div>
  <div class="abs thumb t3" role="img" aria-label="Thumbnail of smiling woman in black and white"></div>

  <div class="abs cta-row">
    <div class="abs cta-ready">Ready to Get Fit?</div>
    <div class="abs cta-divider"></div>
    <div class="abs cta-line">Let us help you get in the best shape of your life!</div>
    <div class="abs btn-start">Get Started!</div>
  </div>

  <main class="abs content"></main>
  <h2 class="abs believe-title">What We Believe <em>Motivation, Support and Accountability.</em></h2>
  <p class="abs believe-copy">Lorem Ipsum is simply dummy text of the printing and typesetting industry. Lorem Ipsum has been the industry's standard dummy text ever since the 1500s, when an unknown printer took a galley of type and scrambled it to make a type specimen book. It has survived not only five centuries, but also the leap into electronic typesetting, remaining essentially unchanged. It was popularised in the 1960s with the release of Lettrafix sheets containing Lorem Ipsum passages.</p>
  <div class="abs btn btn-believe">Read More</div>

  <div class="abs video"></div>
  <div class="abs video-frame" role="img" aria-label="Video still of a dance fitness class in a mirrored studio"></div>
  <div class="abs video-bar">
    <svg width="196" height="26" viewBox="0 0 196 26">
      <rect x="0" y="0" width="196" height="4" fill="#444"/>
      <rect x="0" y="0" width="32" height="4" fill="#c0282d"/>
      <circle cx="32" cy="2" r="4" fill="#ddd"/>
      <rect x="18" y="9" width="2.5" height="9" fill="#fff"/><rect x="23" y="9" width="2.5" height="9" fill="#fff"/>
      <path d="M44 11 h3 l4 -3 v11 l-4 -3 h-3z" fill="#fff"/>
      <rect x="60" y="13" width="38" height="2" fill="#555"/><rect x="60" y="11" width="3" height="6" fill="#fff"/>
      <text x="106" y="17" font-size="7" fill="#fff" font-family="Arimo,sans-serif">0:14 / 3:25</text>
      <rect x="150" y="10" width="9" height="7" fill="#c0282d"/>
      <path d="M166 17 v-6 h6" stroke="#fff" stroke-width="1.5" fill="none"/>
      <path d="M178 10 h4 M178 10 v4 M190 10 h-4 M190 10 v4 M178 19 h4 M178 19 v-4 M190 19 h-4 M190 19 v-4" stroke="#fff" stroke-width="1.3"/>
    </svg>
  </div>

  <div class="abs card-frame f1"><div class="card-photo" role="img" aria-label="Waist with a measuring tape"></div></div>
  <div class="abs card-frame f2"><div class="card-photo" role="img" aria-label="Woman eating a fresh salad"></div></div>
  <div class="abs card-frame f3"><div class="card-photo" role="img" aria-label="Indoor cycling class"></div></div>

  <h3 class="abs card-title" style="left:88px">SLIM DOWN</h3>
  <h3 class="abs card-title" style="left:281px">NUTRITION</h3>
  <h3 class="abs card-title" style="left:474px">FITNESS</h3>
  <p class="abs card-copy" style="left:88px">Custom Friendbook Page Themes will implement a Friendbook Theme via PressKit dashboard.</p>
  <p class="abs card-copy" style="left:281px">PressKit calendar with Events was build with minimalism and functionality in mind.</p>
  <p class="abs card-copy" style="left:474px">Beautiful Accordion Slideshow will showcase your products or services in a creative way.</p>
  <div class="abs btn card-btn" style="left:209px">Read More</div>
  <div class="abs btn card-btn" style="left:403px">Read More</div>
  <div class="abs btn card-btn" style="left:596px">Read More</div>

  <footer class="site-footer"></footer>
  <h4 class="abs foot-h" style="left:94px;top:934px">Silm down</h4>
  <div class="abs foot-copy" style="left:94px;top:965px;width:166px">
    <p>Lorem Ipsum is simply dummy text of the printing and typesetting industry. Lorem Ipsum has been the industry's standard dummy text ever since the 1500s, when an unknown printer took a galley of type and scrambled it to make a type specimen book.</p>
    <p style="margin-top:8px">It has survived not only five centuries, but also the leap into electronic typesetting, remaining essentially unchanged. It was popularised in the 1960s with the release of Lettrafix sheets containing Lorem Ipsum passages.</p>
    <p style="margin-top:8px">and more recently with desktop publishing software like Pagewise.</p>
  </div>
  <div class="abs foot-rule"></div>
  <div class="abs pill" style="left:189px;top:1106px;width:52px;height:14px;line-height:12px">Read more</div>

  <h4 class="abs foot-h" style="left:297px;top:934px">Connect with us</h4>
  <div class="abs tooltip">Chirper</div>
  <div class="abs soc" style="left:297px" aria-label="Vidlyn"><svg width="14" height="14" viewBox="0 0 14 14"><rect x="1" y="3" width="12" height="8" rx="2" fill="none" stroke="#fff" stroke-width="1.4"/><path d="M6 5.3 V8.7 L8.8 7 Z" fill="#fff"/></svg></div>
  <div class="abs soc" style="left:330px" aria-label="Chirper"><svg width="14" height="14" viewBox="0 0 14 14"><path d="M1.5 2.5 H12.5 V9.5 H6 L3 12 V9.5 H1.5 Z" fill="none" stroke="#fff" stroke-width="1.4"/></svg></div>
  <div class="abs soc" style="left:363px" aria-label="Friendbook"><svg width="14" height="14" viewBox="0 0 14 14"><circle cx="7" cy="4.5" r="2.6" fill="none" stroke="#fff" stroke-width="1.4"/><path d="M2 12.5 A5 4 0 0 1 12 12.5" fill="none" stroke="#fff" stroke-width="1.4"/></svg></div>
  <div class="abs soc" style="left:396px" aria-label="Linkora"><svg width="14" height="14" viewBox="0 0 14 14"><circle cx="3" cy="7" r="1.8" fill="#fff"/><circle cx="11" cy="3" r="1.8" fill="#fff"/><circle cx="11" cy="11" r="1.8" fill="#fff"/><path d="M3 7 L11 3 M3 7 L11 11" stroke="#fff" stroke-width="1.2"/></svg></div>
  <h4 class="abs foot-h" style="left:297px;top:1025px">Newsletter Signup</h4>
  <p class="abs foot-copy" style="left:298px;top:1057px;width:140px;font-size:7.6px;line-height:10px">Lorem ipsum dolor sit amet, consectetur adipisicing elit, sed do eiusmod tempor …</p>
  <div class="abs news-field">Email</div>
  <div class="abs news-btn">Sign up</div>

  <h4 class="abs foot-h" style="left:499px;top:934px">Contact us</h4>
  <div class="abs field" style="top:972px;height:19px;line-height:19px">Name</div>
  <div class="abs field" style="top:999px;height:19px;line-height:19px">Email</div>
  <div class="abs field" style="top:1028px;height:61px"></div>
  <div class="abs pill" style="left:583px;top:1107px;width:52px;height:14px;line-height:12px;font-style:normal">Read more</div>

  <div class="bottom-bar"></div>
  <nav class="abs foot-links"><span>Home</span><span>Fitness</span><span>Nutrition</span><span>Fit Lounge</span><span>Fit Score</span><span>Fit School</span><span>Privacy</span><span>Contact Us</span></nav>
  <div class="abs copyright">Copyright © 2012 - TravlinFit - All rights reserved.</div>

</div>
</body>
</html>
```